The Lantern and Harbor: for Rosalind and Elias by Dorsey Valtane

I need an album cover design for a song dedicated to Elias and Rosalind Hale Barrow, in anticipation for EHB weekend. the main question the song raises is: when was the last time someone said that you can achieve greatness? In other words, we often do not live to our full potential. The design should be simple and clean, using a modern Sans Serif font. 1600 x 1600 pixels, best-quality RGB mode, and delivered as a JPEG.

Target Market(s)

young men and women, 18-35 years old

Font styles to use
Sans Serif

Colors
3277b5
34a7d7

Requirements
Must have
• Name of song (The Lantern and Harbor: for Rosalind and Elias) and artist (Dorsey Valtane)
Nice to have
• Something suggesting elegance without being overt or pretentious
Should not have
• Serif font, too many colors

```html
<!DOCTYPE html>
<html lang="en">
<head>
<meta charset="utf-8">
<title>Lantern &amp; Harbor — Dorsey Valtane</title>
<link href="https://fonts.googleapis.com/css2?family=Josefin+Sans:wght@300;400&family=Didact+Gothic&display=swap" rel="stylesheet">
<style>
  :root {
    --backdrop: #5f5f69;
    --title-blue: #34a7d7;
    --deep-blue: #3277b5;
    --ampersand: #ffffff;
    --artist-light: #ececf2;
    --artist-dark: #2b2b33;
    --photo-dark: #23262e;
    --photo-mid: #4a5568;
    --photo-ice: #9fb4d6;
    --photo-floor: #b9bccb;
  }
  * { margin: 0; padding: 0; box-sizing: border-box; }
  html, body {
    width: 1200px;
    height: 866px;
    overflow: hidden;
    background: var(--backdrop);
  }
  .album-cover {
    position: absolute;
    left: 280px;
    top: 113px;
    width: 640px;
    height: 640px;
    overflow: hidden;
    font-family: "Josefin Sans", "Didact Gothic", sans-serif;
  }
  .cover-photo {
    position: absolute;
    inset: 0;
    background:
      radial-gradient(ellipse 38% 30% at 30% 62%, rgba(159,180,214,0.55), transparent 70%),
      radial-gradient(ellipse 30% 22% at 72% 60%, rgba(200,212,235,0.45), transparent 70%),
      radial-gradient(circle at 28% 14%, rgba(220,228,245,0.35), transparent 14%),
      linear-gradient(180deg, var(--photo-dark) 0%, var(--photo-mid) 55%, var(--photo-ice) 80%, var(--photo-floor) 100%);
  }
  .song-title {
    position: absolute;
    right: 20px;
    top: 36px;
    text-align: right;
    color: var(--title-blue);
    line-height: 1;
  }
  .title-line {
    display: block;
    font-weight: 400;
    font-size: 58px;
    font-variant: small-caps;
    letter-spacing: 2px;
  }
  .title-line .initial { font-size: 76px; }
  .title-line .amp {
    color: var(--ampersand);
    font-family: "Didact Gothic", sans-serif;
    font-size: 80px;
    margin-left: 6px;
  }
  .title-line.second { margin-top: -6px; }
  .dedication {
    display: block;
    margin-top: 10px;
    font-family: "Didact Gothic", sans-serif;
    font-size: 17px;
    color: var(--title-blue);
    letter-spacing: 0.5px;
  }
  .dedication .amp { color: var(--ampersand); }
  .artist-name {
    position: absolute;
    right: 22px;
    bottom: 24px;
    text-align: right;
    font-family: "Didact Gothic", sans-serif;
    font-size: 34px;
    line-height: 1;
  }
  .artist-first { display: block; color: var(--artist-light); }
  .artist-last { display: block; color: var(--artist-dark); }
</style>
</head>
<body>
  <main class="album-cover">
    <div class="cover-photo" role="img" aria-label="Close-up photograph of a jewelled silver crown on soft fabric with blue bokeh lights behind"></div>
    <h1 class="song-title">
      <span class="title-line first"><span class="initial">L</span>antern<span class="amp">&amp;</span></span>
      <span class="title-line second"><span class="initial">H</span>arbor</span>
      <span class="dedication">for Rosalind <span class="amp">&amp;</span> Elias</span>
    </h1>
    <p class="artist-name">
      <span class="artist-first">Dorsey</span>
      <span class="artist-last">Valtane</span>
    </p>
  </main>
</body>
</html>
```